Business card and Stationery for data intelligence company

We need a new design for our business cards and stationery (Business Letter templates and a Quote example on Word, but it MUST work on Google Doc as well).

We are a software company based in Ireland and UK. Our product is "Ovrin", data intelligence platform with beautiful visualizations, graph capabilities (things are interconnected), powerful, flexible, it can manage Big Data and Streaming information. It's modern and relatively open source.
Our company will provide data intelligence for law enforcements, pharmaceuticals, and similar high end customers.

We'll launch a new website soon. At the moment it's http://www.kovar-analytics.example if you want to take a look. This is our youtube channel in case you need it to understand what Ovrin is: https://www.youtube.com/c/kovaranalyticschannel

We changed the logo so please use the logo I attach here.

We'd like the output to be cool and modern but elegant and "business" at the same time. It should inspire simple sophistication, "unity" "intent" "purpose" yet subtly very advanced and innovative.

The name "Ovrin" does NOT refer to sirens (mithological creatures) as well as the warning devices. It means Kinetic Object Vector Analysis Reactor. Please use our logo's colors and if you want to something like the "graph" image.

```html
<!DOCTYPE html>
<html lang="en">
<head>
<meta charset="utf-8">
<title>Ovrin Business Card</title>
<link rel="stylesheet" href="https://fonts.googleapis.com/css2?family=Montserrat:wght@500&family=Open+Sans:wght@400;700&display=swap">
<style>
  :root {
    --backdrop: #d9d9d9;
    --card-light: #ffffff;
    --card-dark: #140d07;
    --accent: #f7ad3a;
    --text-grey: #5c5c5c;
    --text-dark: #2f2f2f;
  }
  html, body {
    margin: 0;
    padding: 0;
    width: 1200px;
    height: 900px;
    overflow: hidden;
    background: var(--backdrop);
  }
  .stage {
    position: relative;
    width: 1200px;
    height: 900px;
  }
  .card {
    position: absolute;
    top: 257px;
    width: 397px;
    height: 397px;
    border-radius: 28px;
    overflow: hidden;
  }
  .card--front { left: 205px; background: var(--card-light); }
  .card--back { left: 653px; background: var(--card-dark); }

  .brand-name {
    font-family: "Montserrat", sans-serif;
    font-weight: 500;
    color: var(--accent);
    letter-spacing: 10px;
    line-height: 1;
    margin: 0;
  }
  .card--front .brand-name {
    position: absolute;
    left: 24px;
    top: 48px;
    font-size: 60px;
  }

  .person {
    position: absolute;
    left: 25px;
    top: 159px;
    font-family: "Open Sans", sans-serif;
  }
  .person__name {
    margin: 0;
    font-size: 19px;
    font-weight: 700;
    color: var(--accent);
    line-height: 24px;
  }
  .person__role {
    margin: 0;
    font-size: 18px;
    color: var(--text-grey);
    line-height: 24px;
  }

  .contact-list {
    position: absolute;
    left: 28px;
    top: 217px;
    margin: 0;
    padding: 0;
    list-style: none;
    font-family: "Open Sans", sans-serif;
    font-size: 17px;
    color: var(--text-dark);
  }
  .contact-list li {
    display: flex;
    align-items: center;
    height: 23.5px;
  }
  .contact-list svg {
    width: 15px;
    height: 15px;
    margin-right: 11px;
    fill: var(--accent);
  }

  .address {
    position: absolute;
    left: 28px;
    top: 323px;
    margin: 0;
    font-family: "Open Sans", sans-serif;
    font-size: 18px;
    line-height: 23px;
    color: var(--text-grey);
    font-style: normal;
  }

  .accent-ring {
    position: absolute;
    left: 0;
    top: 0;
  }

  .back-mark {
    position: absolute;
    left: 136px;
    top: 86px;
  }
  .card--back .brand-name {
    position: absolute;
    left: 0;
    width: 397px;
    top: 234px;
    text-align: center;
    font-size: 62px;
    padding-left: 10px;
    box-sizing: border-box;
  }
  .social-list {
    position: absolute;
    top: 336px;
    left: 132px;
    display: flex;
    gap: 30px;
    margin: 0;
    padding: 0;
    list-style: none;
  }
  .social-list li {
    width: 25px;
    height: 25px;
    border-radius: 4px;
    background: var(--accent);
  }
</style>
</head>
<body>
<main class="stage">
  <section class="card card--front" aria-label="Business card front">
    <svg class="accent-ring" width="397" height="397" viewBox="0 0 397 397" aria-hidden="true">
      <circle cx="405" cy="343" r="151" fill="none" stroke="var(--accent)" stroke-width="22"/>
    </svg>
    <h1 class="brand-name">OVRIN</h1>
    <div class="person">
      <p class="person__name">DANIEL REYES</p>
      <p class="person__role">Managing Director</p>
    </div>
    <ul class="contact-list">
      <li>
        <svg viewBox="0 0 24 24" aria-hidden="true"><path d="M6.6 10.8a15.1 15.1 0 0 0 6.6 6.6l2.2-2.2a1 1 0 0 1 1-.25 11.4 11.4 0 0 0 3.6.6 1 1 0 0 1 1 1V20a1 1 0 0 1-1 1A17 17 0 0 1 3 4a1 1 0 0 1 1-1h3.5a1 1 0 0 1 1 1c0 1.25.2 2.45.6 3.6a1 1 0 0 1-.25 1z"/></svg>
        123-456-7890
      </li>
      <li>
        <svg viewBox="0 0 24 24" aria-hidden="true"><path d="M7 2h8l3 3v4h2a2 2 0 0 1 2 2v9a2 2 0 0 1-2 2H4a2 2 0 0 1-2-2v-9a2 2 0 0 1 2-2h3zm2 2v5h7V6h-2V4zm-3 9v2h2v-2zm4 0v2h2v-2zm4 0v2h2v-2zm-8 4v2h2v-2zm4 0v2h2v-2zm4 0v2h2v-2z"/></svg>
        123-456-7890
      </li>
      <li>
        <svg viewBox="0 0 24 24" aria-hidden="true"><path d="M2 5h20v14H2zm2 2v.5l8 5.5 8-5.5V7z"/></svg>
        info@youremail.com
      </li>
      <li>
        <svg viewBox="0 0 24 24" aria-hidden="true"><circle cx="12" cy="12" r="10"/></svg>
        www.yourweb.com
      </li>
    </ul>
    <address class="address">Addres Line Comes Here,<br>Location Pincode 45215</address>
  </section>

  <section class="card card--back" aria-label="Business card back">
    <svg class="back-mark" width="126" height="126" viewBox="0 0 126 126" aria-hidden="true">
      <circle cx="63" cy="63" r="55" fill="none" stroke="var(--accent)" stroke-width="14"/>
    </svg>
    <p class="brand-name">OVRIN</p>
    <ul class="social-list" aria-label="Social profiles">
      <li></li>
      <li></li>
      <li></li>
    </ul>
  </section>
</main>
</body>
</html>
```